E learning Platform for privacy

Current website is as below and its more of a shell.
I need someone to take the text and content and design it properly.
https://study.norvalhub.example/

After that, design has to be implemented with quillbrick and wordpress
https://quillbrick.example/

```html
<!DOCTYPE html>
<html lang="en">
<head>
<meta charset="utf-8">
<title>Norval Learning Centre</title>
<link href="https://fonts.googleapis.com/css2?family=Josefin+Sans:wght@400;600;700&family=Lato:wght@400;700&family=Courier+Prime&family=Libre+Baskerville&display=swap" rel="stylesheet">
<style>
:root{
  --navy:#0a1045;
  --navy-deep:#07103a;
  --orange:#f0801a;
  --ink:#333a4a;
  --muted:#707784;
  --line:#d9dce3;
  --white:#ffffff;
}
*{box-sizing:border-box;margin:0;padding:0}
html,body{width:1200px;height:5000px;overflow:hidden}
body{position:relative;background:var(--white);font-family:"Lato",sans-serif;color:var(--ink)}
.abs{position:absolute}
.btn{position:absolute;background:var(--orange);color:var(--white);font:700 13px "Lato",sans-serif;display:flex;align-items:center;justify-content:center}
.brand{font:700 58px "Josefin Sans",sans-serif;color:var(--orange);letter-spacing:4px}
.dot{width:26px;height:26px;border-radius:50%;background:#6b6f78;display:inline-block}
.site-header{left:0;top:0;width:1200px;height:105px;background:var(--white)}
.site-header .brand{position:absolute;left:66px;top:26px;font-size:46px}
.main-nav{position:absolute;left:346px;top:48px;display:flex;gap:27px;font:400 13px "Lato",sans-serif;color:#222}
.main-nav .active{color:var(--orange)}
.header-social{position:absolute;left:966px;top:43px;display:flex;gap:12px}
.hero{left:0;top:105px;width:1200px;height:600px}
.hero-text{left:0;top:235px;width:1200px;text-align:center;color:var(--white)}
.hero-brand{font:700 60px "Josefin Sans",sans-serif;letter-spacing:8px;color:var(--white)}
.hero-title{margin-top:40px;font:700 54px "Josefin Sans",sans-serif;color:var(--orange)}
.hero-sub{margin-top:14px;font:400 13px "Lato",sans-serif;letter-spacing:2px}
.btn-ghost{position:absolute;border:1px solid var(--white);color:var(--white);font:400 13px "Lato",sans-serif;display:flex;align-items:center;justify-content:center}
.heading-box{position:absolute;background:var(--navy);color:var(--white);font:700 52px "Josefin Sans",sans-serif;letter-spacing:5px;padding-left:12px;display:flex;align-items:center}
.para{position:absolute;font:400 12px/22px "Lato",sans-serif;color:var(--muted)}
.icon-circle{position:absolute;width:88px;height:88px;border-radius:50%;background:var(--orange)}
.serif-title{position:absolute;font:400 21px "Libre Baskerville",serif;color:#222}
.photo{position:absolute}
.social-orange{position:absolute;top:1190px;left:688px;display:flex;gap:22px}
.social-orange span{width:44px;height:44px;border-radius:50%;background:var(--orange)}
.stats{left:601px;top:1258px;width:549px;height:160px;background:var(--navy);border:4px solid var(--orange);display:flex;justify-content:space-around;align-items:center;color:var(--white);text-align:center}
.stats b{display:block;font:400 46px "Lato",sans-serif;color:var(--orange)}
.stats small{font:400 16px "Lato",sans-serif}
.mono{font-family:"Courier Prime",monospace}
.why-list{left:88px;top:1948px;list-style:none;font:400 14px/18px "Courier Prime",monospace;color:#222;letter-spacing:1px}
.why-list li{position:relative;padding-left:30px;margin-bottom:18px;width:320px}
.why-list svg{position:absolute;left:0;top:2px}
.course-card{position:absolute;width:330px;background:var(--orange);box-shadow:0 4px 12px rgba(0,0,0,.25)}
.course-card .photo{position:static;display:block;width:100%}
.course-card p{color:var(--white);font:400 20px/23px "Josefin Sans",sans-serif;text-align:center;padding:8px 10px 0}
.quote{position:absolute;top:2567px;width:324px;height:220px;text-align:center;font:400 13px/25px "Lato",sans-serif;color:#444;padding:22px 18px}
.quote.featured{background:var(--orange);color:var(--white)}
.author{position:absolute;top:140px;left:70px;display:flex;align-items:center;gap:12px;text-align:left}
.avatar{width:54px;height:54px;border-radius:50%;background:#c9b7a4}
.author b{display:block;font:400 16px "Lato",sans-serif;color:#222}
.featured .author b{color:var(--white)}
.author small{font:400 10px "Lato",sans-serif;letter-spacing:1px}
.contact{left:0;top:2894px;width:1200px;height:1012px;background:linear-gradient(180deg,#0c1a4a,#13244f 60%,#0d1a40)}
.form-card{left:305px;top:3174px;width:588px;height:327px;background:var(--white);border-radius:6px}
.field{position:absolute;border:1px solid #eceef2;font:400 13px "Lato",sans-serif;color:#888;padding:11px 14px}
.info-label{position:absolute;width:300px;text-align:center;color:var(--white);font:400 15px "Lato",sans-serif}
.panel-head{position:absolute;background:var(--navy);color:var(--white);font:700 28px "Josefin Sans",sans-serif;letter-spacing:5px;display:flex;align-items:center;justify-content:center}
.label{position:absolute;font:400 14px "Lato",sans-serif;color:#333}
.input{position:absolute;height:32px;border:1px solid #c8ccd3;font:400 12px "Lato",sans-serif;color:#999;padding:8px 12px}
.footer-col-title{position:absolute;font:400 16px "Lato",sans-serif;color:var(--white)}
.footer-text{position:absolute;font:400 14px/22px "Lato",sans-serif;color:var(--white)}
.links{left:896px;top:4560px;list-style:none;font:400 14px "Lato",sans-serif;color:var(--white)}
.links li{margin-bottom:24px}
.links .active{color:var(--orange)}
.contact-line{position:absolute;left:344px;display:flex;gap:14px;align-items:center;font:400 14px "Lato",sans-serif;color:var(--white)}
.footer-social span{width:32px;height:32px;border-radius:50%;border:2px solid var(--white);background:transparent;display:inline-block;margin-right:8px}
.copyright{left:0;top:4915px;width:1200px;height:85px;background:var(--navy-deep);border-top:1px solid #1f2a5e;color:var(--white);font:400 13px "Lato",sans-serif;display:flex;align-items:center;justify-content:center}
</style>
</head>
<body>

<header class="abs site-header">
  <div class="brand">NORVAL</div>
  <nav class="main-nav">
    <span class="active">HOME</span><span>ABOUT US</span><span>COURSES</span><span>BLOGS</span><span>CONTACT US</span><span>REGISTER</span><span>LOGIN</span>
  </nav>
  <div class="header-social"><span class="dot"></span><span class="dot"></span><span class="dot"></span><span class="dot"></span></div>
</header>

<svg class="abs hero" viewBox="0 0 1200 600" role="img" aria-label="Deep blue photo of a digital security dial and a speaker addressing an audience">
  <defs>
    <radialGradient id="heroGlow" cx="0.45" cy="0.4" r="0.7">
      <stop offset="0" stop-color="#2a5fae"/>
      <stop offset="0.55" stop-color="#163a84"/>
      <stop offset="1" stop-color="#0b1c52"/>
    </radialGradient>
  </defs>
  <polygon points="0,0 1200,0 1200,480 310,600 0,480" fill="url(#heroGlow)"/>
</svg>
<div class="abs hero-text">
  <div class="hero-brand">NORVAL</div>
  <div class="hero-title">DATA PROTECTION EXCELLENCE</div>
  <div class="hero-sub">LARGEST ONLINE E-LEARNING RESOURCE FOR DATA PROTECTION &amp; PRIVACY</div>
</div>
<div class="btn" style="left:449px;top:494px;width:142px;height:38px;font-weight:400">Get Trained</div>
<div class="btn-ghost" style="left:610px;top:494px;width:148px;height:38px">Get In Touch</div>

<div class="heading-box" style="left:49px;top:762px;width:551px;height:70px">ABOUT NORVAL</div>
<p class="para" style="left:49px;top:852px;width:551px">Calverin was founded by principals in a Northern California engineering firm and a California-certified public accounting firm in response for a desire to decrease the cost of employer medical insurance. The realities and the economics of employer health insurance in today's economy are daunting.</p>
<div class="btn" style="left:49px;top:982px;width:142px;height:38px">Learn More</div>
<svg class="photo" style="left:611px;top:832px" width="530" height="298" role="img" aria-label="Photo of two women smiling at a tablet in a bright office">
  <defs><linearGradient id="aboutPhoto" x1="0" y1="0" x2="1" y2="1"><stop offset="0" stop-color="#8a5a44"/><stop offset="0.5" stop-color="#d9c9bd"/><stop offset="1" stop-color="#efe9e4"/></linearGradient></defs>
  <rect width="530" height="298" fill="url(#aboutPhoto)"/>
  <circle cx="265" cy="149" r="38" fill="none" stroke="#fff" stroke-width="3" opacity=".8"/>
  <polygon points="254,130 254,168 284,149" fill="#fff" opacity=".8"/>
</svg>
<div class="icon-circle" style="left:57px;top:1046px"></div>
<svg class="abs" style="left:78px;top:1068px" width="46" height="44" viewBox="0 0 46 44"><polygon points="4,40 18,18 26,30 32,22 42,40" fill="#fff"/><line x1="20" y1="18" x2="20" y2="2" stroke="#fff" stroke-width="2"/><polygon points="20,2 30,6 20,10" fill="#fff"/></svg>
<div class="icon-circle" style="left:333px;top:1046px"></div>
<svg class="abs" style="left:360px;top:1064px" width="34" height="52" viewBox="0 0 34 52"><path d="M17 2 C26 10 26 26 23 34 H11 C8 26 8 10 17 2Z" fill="#fff"/><circle cx="17" cy="18" r="4" fill="#f0801a"/><path d="M11 34 L5 42 L12 40Z M23 34 L29 42 L22 40Z" fill="#fff"/><path d="M14 38 L17 50 L20 38Z" fill="#fff"/></svg>
<div class="serif-title" style="left:57px;top:1162px">Our Vision</div>
<div class="serif-title" style="left:333px;top:1162px">Our Mission</div>
<p class="para" style="left:57px;top:1204px;width:252px">Our ownership and management team are comprised of highly-educated and experienced entrepreneurs and professionals. We have more than twenty years of experience in the captive insurance industry and our lead benefits consultant is at the forefront of group captive healthcare management.</p>
<p class="para" style="left:333px;top:1204px;width:258px">We are the gold standard provider for group health captive services, including claims control, wellness programs and provider management in the United States. Our program is unique in that it integrates seamlessly into an employer's existing coverage thus alleviating concerns over disruption to employees' existing provider networks.</p>
<div class="btn" style="left:49px;top:1440px;width:142px;height:36px">Learn More</div>
<div class="social-orange"><span></span><span></span><span></span><span></span><span></span><span></span></div>
<div class="abs stats">
  <div><b>6000+</b><small>STUDENTS</small></div>
  <div><b>114+</b><small>LESSONS</small></div>
  <div><b>170+</b><small>VIDEOS</small></div>
</div>

<div class="heading-box" style="left:84px;top:1618px;width:332px;height:132px;line-height:54px;font-size:54px;padding-left:14px">NORVAL<br>COURSES</div>
<p class="abs mono" style="left:88px;top:1768px;width:290px;font-size:15px;line-height:17px;letter-spacing:2px;color:#333">Ne quis mediocrem sit, dolor repriique nec id, quo no scaevola.</p>
<div class="heading-box" style="left:84px;top:1873px;width:332px;height:55px;font-size:30px;letter-spacing:4px;padding-left:14px">WHY NORVAL?</div>
<ul class="abs why-list">
  <li><svg width="16" height="14"><polyline points="1,7 6,12 15,2" fill="none" stroke="#f0801a" stroke-width="3"/></svg>Comprehensive Roadmap</li>
  <li><svg width="16" height="14"><polyline points="1,7 6,12 15,2" fill="none" stroke="#f0801a" stroke-width="3"/></svg>Operational Perspective</li>
  <li><svg width="16" height="14"><polyline points="1,7 6,12 15,2" fill="none" stroke="#f0801a" stroke-width="3"/></svg>Academic &amp; International Certification</li>
  <li><svg width="16" height="14"><polyline points="1,7 6,12 15,2" fill="none" stroke="#f0801a" stroke-width="3"/></svg>Modular Approach &amp; Flexibility</li>
  <li><svg width="16" height="14"><polyline points="1,7 6,12 15,2" fill="none" stroke="#f0801a" stroke-width="3"/></svg>Network with other peers</li>
  <li><svg width="16" height="14"><polyline points="1,7 6,12 15,2" fill="none" stroke="#f0801a" stroke-width="3"/></svg>Business and Job Opportunities</li>
</ul>
<div class="btn" style="left:88px;top:2229px;width:142px;height:37px">Learn More</div>

<div class="course-card" style="left:436px;top:1702px;height:249px">
  <svg class="photo" width="330" height="178" role="img" aria-label="Photo of a woman touching a glowing network interface"><defs><linearGradient id="c1" x1="0" y1="0" x2="1" y2="1"><stop offset="0" stop-color="#6fa9c9"/><stop offset="1" stop-color="#dcecf3"/></linearGradient></defs><rect width="330" height="178" fill="url(#c1)"/></svg>
  <p>HOW TO SCALE<br>SOCIAL IMPACT</p>
</div>
<div class="course-card" style="left:436px;top:1970px;height:244px">
  <svg class="photo" width="330" height="175" role="img" aria-label="Photo of a hand holding a card with a padlock against a sky and skyscrapers"><defs><linearGradient id="c2" x1="0" y1="0" x2="0" y2="1"><stop offset="0" stop-color="#3f86c8"/><stop offset="1" stop-color="#cfe3f3"/></linearGradient></defs><rect width="330" height="175" fill="url(#c2)"/></svg>
  <p>GLOBAL SOCIAL<br>ENTREPRENEURSHIP</p>
</div>
<div class="course-card" style="left:782px;top:1585px;height:259px">
  <svg class="photo" width="330" height="188" role="img" aria-label="Photo of a finger pressing a padlock icon on a security diagram"><defs><linearGradient id="c3" x1="0" y1="0" x2="1" y2="1"><stop offset="0" stop-color="#8fa9c6"/><stop offset="1" stop-color="#e7edf3"/></linearGradient></defs><rect width="330" height="188" fill="url(#c3)"/></svg>
  <p>NORVAL DEMONSTRATION<br>COURSE</p>
</div>
<div class="course-card" style="left:782px;top:1863px;height:253px">
  <svg class="photo" width="330" height="183" role="img" aria-label="Photo of a hooded figure at a laptop in darkness"><defs><radialGradient id="c4" cx="0.5" cy="0.4" r="0.7"><stop offset="0" stop-color="#4a4a4a"/><stop offset="1" stop-color="#050505"/></radialGradient></defs><rect width="330" height="183" fill="url(#c4)"/></svg>
  <p>HOW TO PROTECT DATA FROM<br>HACKER</p>
</div>

<div class="heading-box" style="left:74px;top:2400px;width:1046px;height:78px;justify-content:center;padding:0;font-size:50px;letter-spacing:6px">TESTIMONIES</div>
<div class="quote" style="left:88px">Click edit button to change this text. Lorem ipsum dolor sit amet, consectetur adipiscing elit. Ut elit tellus, luctus nec ullamcorper mattis, pulvinar dapibus leo.
  <div class="author"><svg class="avatar" role="img" aria-label="Portrait photo of the reviewer"><rect width="54" height="54" fill="#b8a38c"/></svg><div><b>Ada Brennick</b><small>DESIGNER</small></div></div>
</div>
<div class="quote featured" style="left:438px">Click edit button to change this text. Lorem ipsum dolor sit amet, consectetur adipiscing elit. Ut elit tellus, luctus nec ullamcorper mattis, pulvinar dapibus leo.
  <div class="author"><svg class="avatar" role="img" aria-label="Portrait photo of the reviewer"><rect width="54" height="54" fill="#e8d8c8"/></svg><div><b>Lena Corvath</b><small>DESIGNER</small></div></div>
</div>
<div class="quote" style="left:792px">Click edit button to change this text. Lorem ipsum dolor sit amet, consectetur adipiscing elit. Ut elit tellus, luctus nec ullamcorper mattis, pulvinar dapibus leo.
  <div class="author"><svg class="avatar" role="img" aria-label="Portrait photo of the reviewer"><rect width="54" height="54" fill="#9c8c80"/></svg><div><b>Owen Tarrel</b><small>DESIGNER</small></div></div>
</div>

<div class="abs contact" role="img" aria-label="Dark blue tinted photo of a desk with a telephone"></div>
<div class="heading-box" style="left:286px;top:2986px;width:620px;height:130px;justify-content:center;text-align:center;padding:0;line-height:54px">LET'S GET IN<br>TOUCH</div>
<div class="abs form-card">
  <div class="field" style="left:42px;top:42px;width:244px;height:42px">First Name</div>
  <div class="field" style="left:304px;top:42px;width:244px;height:42px">Last Name</div>
  <div class="field" style="left:42px;top:94px;width:506px;height:42px">Email Address</div>
  <div class="field" style="left:42px;top:140px;width:506px;height:94px">Message</div>
  <div class="btn" style="left:42px;top:244px;width:506px;height:42px;font-weight:400;font-size:14px">SUBMIT</div>
</div>
<div class="icon-circle" style="left:417px;top:3552px;width:56px;height:56px"></div>
<svg class="abs" style="left:432px;top:3570px" width="26" height="20"><rect x="1" y="1" width="24" height="18" rx="2" fill="#fff"/><polyline points="2,3 13,11 24,3" fill="none" stroke="#f0801a" stroke-width="2"/></svg>
<div class="icon-circle" style="left:726px;top:3552px;width:56px;height:56px"></div>
<svg class="abs" style="left:741px;top:3567px" width="26" height="26" viewBox="0 0 24 24"><path d="M6.6 10.8c1.4 2.8 3.8 5.1 6.6 6.6l2.2-2.2c.3-.3.7-.4 1-.2 1.1.4 2.3.6 3.6.6.6 0 1 .4 1 1V20c0 .6-.4 1-1 1C10.6 21 3 13.4 3 4c0-.6.4-1 1-1h3.5c.6 0 1 .4 1 1 0 1.3.2 2.5.6 3.6.1.3 0 .7-.2 1l-2.3 2.2z" fill="#fff"/></svg>
<div class="info-label" style="left:295px;top:3616px">Email Address</div>
<div class="info-label" style="left:604px;top:3616px">Call Us</div>
<div class="info-label" style="left:295px;top:3656px;font-size:14px">support@norvalhub.example</div>
<div class="info-label" style="left:604px;top:3656px;font-size:14px">+13-555-0100</div>
<div class="abs" style="left:301px;top:3705px;width:570px;height:2px;background:var(--orange)"></div>
<div class="abs" style="left:301px;top:3752px;width:3px;height:72px;background:var(--orange)"></div>
<div class="abs" style="left:316px;top:3756px;font:700 29px/34px 'Josefin Sans',sans-serif;letter-spacing:3px;color:#fff">OUR SOCIAL<br>MEDIA</div>
<div class="abs" style="left:687px;top:3780px;display:flex;gap:14px"><span class="dot" style="width:16px;height:16px;background:#fff"></span><span class="dot" style="width:16px;height:16px;background:#fff"></span><span class="dot" style="width:16px;height:16px;background:#fff"></span><span class="dot" style="width:16px;height:16px;background:#fff"></span><span class="dot" style="width:16px;height:16px;background:#fff"></span></div>

<div class="panel-head" style="left:84px;top:3987px;width:506px;height:53px">REGISTER</div>
<div class="panel-head" style="left:603px;top:3987px;width:508px;height:53px">LOG IN</div>
<div class="label" style="left:88px;top:4066px">Name</div>
<div class="input" style="left:88px;top:4086px;width:502px">Name</div>
<div class="label" style="left:88px;top:4136px">Email</div>
<div class="input" style="left:88px;top:4156px;width:502px">Email</div>
<div class="label" style="left:88px;top:4206px">Enter Password</div>
<div class="input" style="left:88px;top:4226px;width:502px">Password</div>
<div class="label" style="left:88px;top:4276px">Conform Password</div>
<div class="input" style="left:88px;top:4296px;width:502px">Retype Password</div>
<div class="btn" style="left:88px;top:4341px;width:502px;height:32px;font-weight:400;font-size:12px">Submit</div>

<div class="label" style="left:609px;top:4066px">Username or Email Address</div>
<div class="input" style="left:609px;top:4086px;width:502px">Username or Email Address</div>
<div class="label" style="left:609px;top:4136px">Password</div>
<div class="input" style="left:609px;top:4156px;width:502px">Password</div>
<svg class="abs" style="left:1072px;top:4093px" width="20" height="20"><circle cx="10" cy="10" r="8" fill="none" stroke="#555" stroke-width="1.5"/></svg>
<svg class="abs" style="left:1072px;top:4163px" width="20" height="20"><circle cx="10" cy="10" r="8" fill="none" stroke="#555" stroke-width="1.5"/></svg>
<div class="abs" style="left:609px;top:4205px;width:10px;height:10px;border:1px solid #999"></div>
<div class="label" style="left:624px;top:4203px;font-size:11px">Remember Me</div>
<div class="btn" style="left:609px;top:4232px;width:78px;height:32px;background:#7a8190;font-weight:400;font-size:12px">Log In</div>
<div class="label" style="left:609px;top:4282px;font-size:11px;color:var(--orange)">Lost your password?</div>

<svg class="abs" style="left:0;top:4395px" width="1200" height="520" viewBox="0 0 1200 520"><polygon points="0,60 175,0 1200,100 1200,520 0,520" fill="var(--navy)"/></svg>
<div class="abs brand" style="left:78px;top:4526px;color:#fff;font-size:46px">NORVAL</div>
<p class="footer-text" style="left:78px;top:4636px;width:240px;font-size:13px">Natus eget occaecati, lobortis, vestibulum nam eros, risus lacinia lacus.Lorem accusantium.</p>
<div class="abs footer-social" style="left:78px;top:4762px"><span></span><span></span><span></span><span></span></div>
<div class="footer-col-title" style="left:344px;top:4526px">Contact Details</div>
<div class="contact-line" style="top:4614px"><svg width="16" height="20" viewBox="0 0 16 20"><path d="M8 0C3.6 0 0 3.5 0 7.8 0 13.6 8 20 8 20s8-6.4 8-12.2C16 3.5 12.4 0 8 0z" fill="#f0801a"/><circle cx="8" cy="8" r="3" fill="#0a1045"/></svg>48, Harlow Square, Eastbridge</div>
<div class="contact-line" style="top:4658px"><svg width="18" height="18" viewBox="0 0 24 24"><path d="M6.6 10.8c1.4 2.8 3.8 5.1 6.6 6.6l2.2-2.2c.3-.3.7-.4 1-.2 1.1.4 2.3.6 3.6.6.6 0 1 .4 1 1V20c0 .6-.4 1-1 1C10.6 21 3 13.4 3 4c0-.6.4-1 1-1h3.5c.6 0 1 .4 1 1 0 1.3.2 2.5.6 3.6.1.3 0 .7-.2 1l-2.3 2.2z" fill="#f0801a"/></svg>44 210-555-0193/94</div>
<div class="contact-line" style="top:4702px"><svg width="14" height="20"><rect x="1" y="0" width="12" height="20" rx="2" fill="#f0801a"/></svg>(003) 555-0148</div>
<div class="contact-line" style="top:4748px"><svg width="20" height="15"><rect x="0" y="0" width="20" height="15" rx="1" fill="#f0801a"/><polyline points="1,2 10,9 19,2" fill="none" stroke="#0a1045" stroke-width="1.5"/></svg>info@norvalhub.example</div>
<div class="footer-col-title" style="left:599px;top:4518px">Subscribe For Latest Update</div>
<div class="input" style="left:601px;top:4608px;width:242px;height:40px;background:#fff;border:none;padding-top:12px">Email</div>
<div class="input" style="left:601px;top:4668px;width:242px;height:104px;background:#fff;border:none">Message</div>
<div class="btn" style="left:601px;top:4794px;width:158px;height:38px;font-weight:400;font-size:13px">Send Message</div>
<div class="footer-col-title" style="left:877px;top:4518px">Important Links</div>
<div class="abs" style="left:877px;top:4592px;width:253px;height:2px;background:#8a90ad"></div>
<ul class="abs links" style="top:4562px">
  <li class="active">HOME</li><li>ABOUT US</li><li>COURSES</li><li>BLOGS</li><li>CONTACT US</li><li>REGISTER</li><li>LOGIN</li>
</ul>
<div class="abs copyright">Copyright © 2020 norvalhub | Powered by norvalhub</div>

</body>
</html>
```